Stationery Design Project

We are a VOIP, hosted pbx, and cloud services provider. Clients are mostly hotels, offices, business etc. needing phone services.

Our Slogan is : "Clear calls & fair prices for every business"

the logo is attached
the address is
6127 Marrow Pkwy, suite 310
Dallas TX 75318

Phone: 000-000-0000
Fax: 000-000-0000
Website: Pravicon.com

```html
<!DOCTYPE html>
<html lang="en">
<head>
<meta charset="utf-8">
<title>Pravicon Stationery</title>
<link href="https://fonts.googleapis.com/css2?family=Exo+2:wght@600;700&family=Open+Sans:wght@400;600&display=swap" rel="stylesheet">
<style>
  :root {
    --stage: #2b2b2b;
    --page: #ffffff;
    --lime: #a7cf45;
    --ink: #3a3a3a;
    --flap-edge: #1e2a10;
    --fold: #d9d9d9;
    --mark: #f25a9a;
  }
  * { box-sizing: border-box; margin: 0; padding: 0; }
  html, body { width: 1200px; height: 900px; overflow: hidden; background: #fff; }
  .canvas { position: relative; width: 1200px; height: 900px; }
  .stage { position: absolute; left: 36px; top: 24px; width: 1134px; height: 852px; background: var(--stage); }

  .brand { display: flex; align-items: center; gap: 10px; }
  .brand-square { background: var(--mark); flex: none; }
  .brand-name { font-family: "Exo 2", sans-serif; font-weight: 700; color: var(--ink); line-height: 1; }
  .slogan { font-family: "Exo 2", sans-serif; font-weight: 600; color: var(--ink); white-space: nowrap; }
  .info { font-family: "Open Sans", sans-serif; white-space: nowrap; }

  /* Letterhead */
  .letterhead { position: absolute; left: 90px; top: 60px; width: 590px; height: 790px; background: var(--page); overflow: hidden; box-shadow: 8px 8px 0 rgba(0,0,0,.25); }
  .letterhead .brand { position: absolute; left: 26px; top: 22px; }
  .letterhead .brand-square { width: 56px; height: 76px; }
  .letterhead .brand-name { font-size: 40px; }
  .letterhead .slogan { position: absolute; left: 80px; top: 100px; font-size: 11px; }
  .letterhead .wave { position: absolute; left: 0; bottom: 0; }
  .letterhead .site { position: absolute; left: 10px; bottom: 10px; font-family: "Open Sans", sans-serif; font-size: 17px; color: #fff; }
  .letterhead .address { position: absolute; right: 10px; bottom: 8px; text-align: right; font-size: 10px; color: var(--ink); line-height: 1.4; }
  .letterhead .address .gap { margin-top: 10px; }

  /* Business card front */
  .card { position: absolute; background: var(--lime); box-shadow: 4px 4px 0 rgba(0,0,0,.3); }
  .card-front { left: 640px; top: 140px; width: 230px; height: 170px; }
  .card-front .mark-area { position: absolute; right: 12px; top: 12px; width: 82px; height: 146px; background: var(--mark); }
  .card-front .info { position: absolute; left: 8px; top: 110px; font-size: 8px; color: #fff; line-height: 1.3; }
  .card-front .info .gap { margin-top: 9px; }

  /* Business card back */
  .card-back { left: 826px; top: 326px; width: 288px; height: 164px; }
  .card-back .brand { position: absolute; left: 34px; top: 44px; }
  .card-back .brand-square { width: 28px; height: 40px; }
  .card-back .brand-name { font-size: 24px; }
  .card-back .slogan { position: absolute; left: 68px; top: 90px; font-size: 8px; }
  .card-back .site { position: absolute; right: 40px; bottom: 22px; font-family: "Open Sans", sans-serif; font-size: 8px; color: #fff; }

  /* Envelope */
  .envelope { position: absolute; left: 692px; top: 536px; width: 470px; height: 256px; box-shadow: -8px 8px 0 rgba(0,0,0,.3); }
  .envelope svg { position: absolute; inset: 0; }
  .envelope .brand { position: absolute; left: 178px; top: 28px; gap: 6px; }
  .envelope .brand-square { width: 18px; height: 26px; }
  .envelope .brand-name { font-size: 16px; }
  .envelope .slogan { position: absolute; left: 0; right: 0; text-align: center; top: 60px; font-size: 6px; }
  .envelope .site { position: absolute; left: 0; right: 0; top: 224px; text-align: center; font-family: "Open Sans", sans-serif; font-size: 17px; color: var(--ink); }
</style>
</head>
<body>
<div class="canvas">
  <div class="stage"></div>

  <section class="letterhead">
    <div class="brand">
      <span class="brand-square" role="img" aria-label="Brand mark"></span>
      <span class="brand-name">Pravicon</span>
    </div>
    <p class="slogan">Clear calls &amp; fair prices for every business</p>
    <svg class="wave" width="590" height="130" viewBox="0 0 590 130">
      <path d="M0 10 Q300 60 470 130 L0 130 Z" fill="var(--lime)"/>
    </svg>
    <p class="site">www.pravicon.com</p>
    <div class="info address">
      <p>6127 Marrow Pkwy, suite 310</p>
      <p>Dallas TX 75318</p>
      <p class="gap">Phone: 000-000-0000</p>
      <p>Fax: 000-000-0000</p>
    </div>
  </section>

  <section class="card card-front">
    <div class="mark-area" role="img" aria-label="Brand mark"></div>
    <div class="info">
      <p>6127 Marrow Pkwy, suite 310</p>
      <p>Dallas TX 75318</p>
      <p class="gap">Phone: 000-000-0000</p>
      <p>Fax: 000-000-0000</p>
    </div>
  </section>

  <section class="card card-back">
    <div class="brand">
      <span class="brand-square" role="img" aria-label="Brand mark"></span>
      <span class="brand-name">Pravicon</span>
    </div>
    <p class="slogan">Clear calls &amp; fair prices for every business</p>
    <p class="site">www.pravicon.com</p>
  </section>

  <section class="envelope">
    <svg width="470" height="256" viewBox="0 0 470 256">
      <rect x="0" y="0" width="470" height="256" fill="var(--page)"/>
      <path d="M0 256 L180 110 M470 256 L290 110" stroke="var(--fold)" stroke-width="2" fill="none"/>
      <path d="M0 0 L470 0 L464 14 L235 120 L6 14 Z" fill="var(--lime)" stroke="var(--flap-edge)" stroke-width="3" stroke-linejoin="round"/>
    </svg>
    <div class="brand">
      <span class="brand-square" role="img" aria-label="Brand mark"></span>
      <span class="brand-name">Pravicon</span>
    </div>
    <p class="slogan">Clear calls &amp; fair prices for every business</p>
    <p class="site">www.pravicon.com</p>
  </section>
</div>
</body>
</html>
```